Business Card Design for Real Estate Company

I am looking for a business card design that will catch my client's attention.

Industry/Entity Type

Business

Requirements
Must have
• Please have the following information in the business card design. You can substitute the "Office, Mobile, email, and web" with an icon or some other design you may think will go well with the business card.

Derek Osmund
482 W. Fenwick St., Suite 310
Pasadena, CA 91348
Office: 626.748.1196
Mobile: 626.913.4071
email: Derek@CrestviewPropertyWalk.example
web: www.CrestviewPropertyWalk.example

```html
<!DOCTYPE html>
<html lang="en">
<head>
<meta charset="utf-8">
<title>Crestview Property Walk – Business Card Layout</title>
<link href="https://fonts.googleapis.com/css2?family=Montserrat:wght@400;500;600&family=Open+Sans:wght@400;600&display=swap" rel="stylesheet">
<style>
  :root {
    --page: #ffffff;
    --guide: #333333;
    --blue-light: #2f8fe0;
    --blue-mid: #1565c8;
    --blue-deep: #0b3f8f;
    --ink-white: #ffffff;
    --ink-soft: #dfe9f7;
    --charcoal: #3a3a3a;
    --charcoal-dark: #1c1c1c;
    --charcoal-band: #111111;
    --silver: #d8d8d8;
    --cyan: #1ea7e4;
    --magenta: #e2138c;
    --yellow: #f4e61b;
    --black-swatch: #0d0d0d;
  }
  * { box-sizing: border-box; margin: 0; padding: 0; }
  html, body { width: 1200px; height: 1019px; overflow: hidden; background: var(--page); }
  body { position: relative; font-family: "Open Sans", Arial, sans-serif; }

  .guides { position: absolute; inset: 0; }
  .dimension-label {
    position: absolute; font-family: "Open Sans", Arial, sans-serif;
    font-size: 20px; color: var(--guide); background: var(--page); padding: 0 6px;
  }
  .dimension-width { left: 256px; top: 14px; }
  .dimension-height { left: 528px; top: 182px; }

  .card { position: absolute; overflow: hidden; }

  .brand { display: flex; align-items: center; gap: 10px; color: var(--ink-white); white-space: nowrap;
    font-family: "Montserrat", Arial, sans-serif; font-weight: 500; }
  .brand-dot { width: 16px; height: 16px; border-radius: 50%; background: var(--ink-white); flex: none; }

  /* Blue front */
  .card-front {
    left: 72px; top: 72px; width: 424px; height: 258px;
    background: linear-gradient(160deg, var(--blue-light) 0%, var(--blue-mid) 55%, var(--blue-deep) 100%);
  }
  .card-front .contact-band {
    position: absolute; left: 0; right: 0; bottom: 0; height: 104px;
    background: linear-gradient(180deg, rgba(5,40,110,0.75), rgba(5,35,95,0.9));
  }
  .card-front .holder { position: absolute; right: 30px; top: 40px; text-align: right; color: var(--ink-white); }
  .holder .name { font-family: "Montserrat", Arial, sans-serif; font-size: 18px; font-weight: 500; }
  .holder .role { font-size: 10px; color: var(--ink-soft); margin-top: 2px; margin-right: 18px; }
  .card-front .brand { position: absolute; left: 40px; top: 100px; font-size: 21px; }

  .contact-text { position: absolute; color: var(--ink-soft); font-size: 9.5px; line-height: 19px; white-space: nowrap; }
  .card-front .address { left: 30px; top: 170px; }
  .card-front .lines { left: 236px; top: 170px; }

  /* Blue back */
  .card-back-blue {
    left: 680px; top: 72px; width: 416px; height: 254px;
    background: linear-gradient(160deg, var(--blue-light) 0%, var(--blue-mid) 60%, var(--blue-deep) 100%);
  }
  .card-back-blue .emblem-area {
    position: absolute; left: 178px; top: 28px; width: 60px; height: 60px; border-radius: 50%;
    background: radial-gradient(circle, rgba(255,255,255,0.35), rgba(255,255,255,0));
  }
  .card-back-blue .brand { position: absolute; left: 0; right: 0; top: 124px; justify-content: center; font-size: 24px; }

  .section-label { position: absolute; left: 160px; top: 640px; font-size: 19px; color: #222; line-height: 23px; }

  /* Dark cards */
  .card-dark {
    left: 304px; width: 482px;
    background: radial-gradient(ellipse at 50% 40%, var(--charcoal) 0%, var(--charcoal-dark) 100%);
  }
  .card-dark-logo { top: 410px; height: 280px; }
  .card-dark-logo .top-strip { position: absolute; left: 0; right: 0; top: 0; height: 14px; background: var(--charcoal-band); }
  .card-dark-logo .bottom-strip { position: absolute; left: 0; right: 0; bottom: 0; height: 30px; background: var(--charcoal-band); }
  .swatches { position: absolute; left: 128px; top: 88px; display: flex; gap: 24px; }
  .swatch { width: 32px; height: 32px; border: 3px solid #555; box-shadow: 0 2px 4px rgba(0,0,0,0.6); }
  .swatch.cyan { background: var(--cyan); }
  .swatch.magenta { background: var(--magenta); }
  .swatch.yellow { background: var(--yellow); }
  .swatch.black { background: var(--black-swatch); }
  .sheen-line { position: absolute; left: 40px; right: 40px; top: 136px; height: 2px;
    background: linear-gradient(90deg, transparent, var(--silver), transparent); }
  .card-dark-logo .brand { position: absolute; left: 0; right: 0; top: 176px; justify-content: center; font-size: 24px; color: var(--silver); }
  .card-dark-logo .brand-dot { background: var(--silver); }

  .card-dark-contact { top: 700px; height: 290px; }
  .contact-row { position: absolute; left: 0; display: flex; align-items: center; }
  .tab { width: 38px; height: 30px; font-size: 8px; color: #fff; display: flex; align-items: center; justify-content: center; flex: none; }
  .tab.cyan { background: var(--cyan); }
  .tab.magenta { background: var(--magenta); }
  .tab.yellow { background: var(--yellow); color: #222; }
  .tab.black { background: var(--black-swatch); border: 1px solid #555; }
  .row-text { margin-left: 12px; color: #f2f2f2; font-size: 13px; line-height: 18px; white-space: nowrap; }
  .row-address { top: 58px; }
  .row-phone { top: 106px; }
  .row-email { top: 156px; }
  .row-web { top: 206px; }
  .divider { position: absolute; left: 268px; top: 10px; bottom: 10px; width: 2px;
    background: linear-gradient(180deg, transparent, var(--silver), transparent); }
  .card-dark-contact .holder-large { position: absolute; left: 290px; top: 100px; width: 176px; text-align: center;
    font-family: "Montserrat", Arial, sans-serif; font-size: 34px; line-height: 44px; color: #eeeeee; }
</style>
</head>
<body>
  <svg class="guides" width="1200" height="1019" aria-hidden="true">
    <g stroke="var(--guide)" stroke-width="1.2" fill="none">
      <line x1="88" y1="0" x2="88" y2="56"/><line x1="480" y1="0" x2="480" y2="56"/>
      <line x1="88" y1="28" x2="480" y2="28"/>
      <line x1="504" y1="84" x2="570" y2="84"/><line x1="504" y1="318" x2="570" y2="318"/>
      <line x1="546" y1="84" x2="546" y2="318"/>
      <line x1="0" y1="84" x2="46" y2="84"/><line x1="0" y1="318" x2="46" y2="318"/>
      <line x1="88" y1="344" x2="88" y2="400"/><line x1="480" y1="344" x2="480" y2="400"/>
      <line x1="612" y1="84" x2="664" y2="84"/><line x1="612" y1="318" x2="664" y2="318"/>
      <line x1="1120" y1="84" x2="1176" y2="84"/><line x1="1120" y1="318" x2="1176" y2="318"/>
      <line x1="694" y1="0" x2="694" y2="56"/><line x1="1090" y1="0" x2="1090" y2="56"/>
      <line x1="694" y1="344" x2="694" y2="400"/><line x1="1090" y1="344" x2="1090" y2="400"/>
    </g>
  </svg>
  <span class="dimension-label dimension-width">3.5”</span>
  <span class="dimension-label dimension-height">2”</span>

  <section class="card card-front">
    <div class="contact-band"></div>
    <div class="holder">
      <p class="name">Derek Osmund</p>
      <p class="role">manager</p>
    </div>
    <div class="brand"><span class="brand-dot"></span>Crestview Property Walk</div>
    <p class="contact-text address">482 W. Fenwick St., Suite 310<br>Pasadena, CA 91348<br>www.CrestviewPropertyWalk.example</p>
    <p class="contact-text lines">626.748.1196<br>626.913.4071<br>Derek@CrestviewPropertyWalk.example</p>
  </section>

  <section class="card card-back-blue">
    <div class="emblem-area" role="img" aria-label="Soft light glow where the brand emblem sits"></div>
    <div class="brand"><span class="brand-dot"></span>Crestview Property Walk</div>
  </section>

  <p class="section-label">BACK<br>DEsign</p>

  <section class="card card-dark card-dark-logo">
    <div class="top-strip"></div>
    <div class="swatches">
      <span class="swatch cyan"></span><span class="swatch magenta"></span>
      <span class="swatch yellow"></span><span class="swatch black"></span>
    </div>
    <div class="sheen-line"></div>
    <div class="brand"><span class="brand-dot"></span>Crestview Property Walk</div>
    <div class="bottom-strip"></div>
  </section>

  <section class="card card-dark card-dark-contact">
    <div class="contact-row row-address"><span class="tab cyan">office</span><p class="row-text">482 W. Fenwick St., Suite 310</p></div>
    <div class="contact-row row-phone"><span class="tab magenta">phone</span><p class="row-text">Office: 626.748.1196<br>Mobile: 626.913.4071</p></div>
    <div class="contact-row row-email"><span class="tab yellow">e-mail</span><p class="row-text">Derek@CrestviewPropertyWalk<br>.example</p></div>
    <div class="contact-row row-web"><span class="tab black">web</span><p class="row-text">www.CrestviewPropertyWalk<br>.example</p></div>
    <div class="divider"></div>
    <p class="holder-large">Derek<br>Osmund</p>
  </section>
</body>
</html>
```